TRL Cards
Business Cards - Financial Services
Business Cards
Professional
Dominic Hale
Managing Director of Digital Services
387 Marlowe St Suite 204 New York, NY 10017
dhale@trlwealthco.example
www.trlwealthco.example
sarmadshaikh sarmadshaikh
sir its not getting aplosd
ruxanda ruxanda
Please uploud your logo in .ai format

```html
<!DOCTYPE html>
<html lang="en">
<head>
<meta charset="utf-8">
<title>TRL Cards – Business Card Design</title>
<link rel="stylesheet" href="https://fonts.googleapis.com/css2?family=Montserrat:wght@400;500;600&display=swap">
<style>
  :root {
    --backdrop: #3b3b3d;
    --card-white: #ffffff;
    --brand-green: #1f4f2c;
    --brand-green-dark: #173d21;
    --accent-gold: #b89d68;
    --text-dark: #3a3a3a;
    --text-muted: #6b6b6b;
    --text-light: #ffffff;
  }
  * { margin: 0; padding: 0; box-sizing: border-box; }
  html, body {
    width: 1200px;
    height: 653px;
    overflow: hidden;
    background: var(--backdrop);
    font-family: "Montserrat", sans-serif;
  }
  .stage {
    position: relative;
    width: 1200px;
    height: 653px;
  }
  .card {
    position: absolute;
    width: 520px;
    height: 300px;
    background: var(--card-white);
    overflow: hidden;
  }
  .card--front { left: 60px; top: 176px; }
  .card--back { left: 620px; top: 176px; }

  .brand {
    display: flex;
    align-items: center;
    gap: 10px;
  }
  .brand__dot {
    width: 40px;
    height: 40px;
    border-radius: 50%;
    background: var(--brand-green);
  }
  .brand__name {
    font-weight: 600;
    font-size: 38px;
    letter-spacing: 2px;
    color: var(--brand-green);
    line-height: 1;
  }
  .card--front .brand {
    position: absolute;
    left: 50%;
    top: 50%;
    transform: translate(-50%, -50%);
  }

  .card__shape {
    position: absolute;
    inset: 0;
    width: 100%;
    height: 100%;
  }
  .card--back .brand {
    position: absolute;
    left: 150px;
    top: 36px;
  }
  .card--back .brand__dot { width: 34px; height: 34px; }
  .card--back .brand__name { font-size: 32px; }

  .holder-name {
    position: absolute;
    left: 30px;
    bottom: 30px;
    color: var(--text-light);
    font-size: 13px;
    font-weight: 500;
    letter-spacing: 2px;
    text-transform: uppercase;
  }

  .contact {
    position: absolute;
    right: 24px;
    top: 40px;
    text-align: right;
    color: var(--text-dark);
    font-size: 8.5px;
    line-height: 1.5;
  }
  .contact__address { margin-bottom: 22px; max-width: 130px; margin-left: auto; }
  .contact__list { list-style: none; }
  .contact__item {
    display: flex;
    justify-content: flex-end;
    align-items: center;
    gap: 6px;
    color: var(--text-muted);
    margin-bottom: 3px;
  }
  .contact__icon {
    width: 8px;
    height: 8px;
    border-radius: 50%;
    background: var(--brand-green);
  }
</style>
</head>
<body>
<main class="stage">
  <section class="card card--front" aria-label="Business card front">
    <div class="brand">
      <span class="brand__dot"></span>
      <span class="brand__name">TRL</span>
    </div>
  </section>

  <section class="card card--back" aria-label="Business card back">
    <svg class="card__shape" viewBox="0 0 520 300" preserveAspectRatio="none" aria-hidden="true">
      <path d="M0,104 C170,112 330,200 440,300 L408,300 C300,214 160,132 0,122 Z" fill="var(--accent-gold)"/>
      <path d="M0,122 C160,132 300,214 408,300 L0,300 Z" fill="var(--brand-green)"/>
    </svg>

    <div class="brand">
      <span class="brand__dot"></span>
      <span class="brand__name">TRL</span>
    </div>

    <div class="contact">
      <p class="contact__address">387 Marlowe St Suite 204<br>New York, NY 10017</p>
      <ul class="contact__list">
        <li class="contact__item">T: 212 555 0147 <span class="contact__icon"></span></li>
        <li class="contact__item">M: 212 555 0182 <span class="contact__icon"></span></li>
        <li class="contact__item">dhale@trlwealthco.example <span class="contact__icon"></span></li>
        <li class="contact__item">www.trlwealthco.example <span class="contact__icon"></span></li>
      </ul>
    </div>

    <p class="holder-name">Dominic Hale</p>
  </section>
</main>
</body>
</html>
```